Copper Wren Beverage Co.

Copper Wren is a new beverage company that currently specializes in energy and hydration. I need label design for the bottles. The label will be a full sleeve so free free to use the entire bottle. The premise behind the product is that its a Copper Wren from the competition. The label needs to say smart, strong, expensive. The background for the label will be black.
Updates

I need an entire label design as well as logo

Target Market(s)

20-30 year old active people.

Industry/Entity Type

It Company

Logo Text

By athletes for the athlete in all of us.

Logo styles of interest
Pictorial/Combination Logo
Wordmark Logo
Requirements
Must have
• the flavors are fruit based. Blackberry lime, mango pineapple, mango berry, strawberry kiwi. Incorporate natural looking fruit into the design.

```html
<!DOCTYPE html>
<html lang="en">
<head>
<meta charset="utf-8">
<title>Copper Wren — Superfruit Energy Drink Label</title>
<link href="https://fonts.googleapis.com/css2?family=Montserrat:wght@400;600;800;900&display=swap" rel="stylesheet">
<style>
  :root {
    --ink: #000000;
    --label: #1e1e1e;
    --white: #ffffff;
    --yellow: #f7d21e;
    --muted: #6a6a6a;
    --leaf: #5f7d2c;
    --leaf-dark: #3e5220;
    --mango-green: #9aae3c;
    --mango-gold: #e9c443;
    --mango-blush: #d9774a;
    --pineapple: #f2df6a;
    --rind: #b98a2f;
  }
  html, body {
    margin: 0;
    width: 1200px;
    height: 900px;
    overflow: hidden;
    background: var(--ink);
    font-family: "Montserrat", sans-serif;
  }
  .canvas {
    position: relative;
    width: 1200px;
    height: 900px;
    background: var(--ink);
  }
  .brand-mark {
    position: absolute;
    left: 130px;
    top: 398px;
    margin: 0;
    color: var(--yellow);
    font-weight: 900;
    font-size: 60px;
    line-height: 1.02;
    letter-spacing: -1px;
    text-transform: uppercase;
  }
  .label {
    position: absolute;
    left: 530px;
    top: 220px;
    width: 200px;
    height: 500px;
    background: var(--label);
    border-radius: 12px;
    color: var(--white);
    text-align: center;
    overflow: hidden;
  }
  .label__tagline {
    position: absolute;
    top: 12px;
    left: 0;
    right: 0;
    margin: 0;
    font-size: 9px;
    font-weight: 800;
    line-height: 1.25;
    text-transform: uppercase;
  }
  .label__fruit {
    position: absolute;
    left: 24px;
    top: 58px;
    width: 160px;
    height: 370px;
    background: linear-gradient(168deg,
      var(--leaf) 0%,
      var(--mango-green) 10%,
      var(--mango-gold) 20%,
      var(--mango-blush) 27%,
      var(--mango-green) 35%,
      var(--leaf-dark) 43%,
      var(--pineapple) 55%,
      var(--mango-gold) 64%,
      var(--mango-blush) 72%,
      var(--mango-green) 80%,
      var(--leaf) 88%,
      var(--rind) 100%);
    -webkit-mask-image: radial-gradient(ellipse 46% 50% at 52% 50%, #000 62%, transparent 100%);
    mask-image: radial-gradient(ellipse 46% 50% at 52% 50%, #000 62%, transparent 100%);
  }
  .label__name {
    position: absolute;
    top: 180px;
    left: 0;
    right: 0;
    margin: 0;
    color: var(--yellow);
    font-weight: 900;
    font-size: 31px;
    line-height: 0.98;
    text-transform: uppercase;
    text-shadow: 0 2px 6px rgba(0, 0, 0, 0.55);
  }
  .flavor {
    position: absolute;
    background: var(--yellow);
    color: var(--ink);
    font-weight: 800;
    font-size: 10.5px;
    line-height: 20px;
    height: 20px;
    text-transform: uppercase;
  }
  .flavor--first { left: 5px; top: 302px; width: 63px; }
  .flavor--second { right: 2px; top: 312px; width: 78px; }
  .label__type {
    position: absolute;
    top: 428px;
    left: 0;
    right: 0;
    margin: 0;
    font-weight: 800;
    font-size: 11.5px;
    text-transform: uppercase;
  }
  .label__type em { font-style: normal; color: var(--yellow); }
  .label__volume {
    position: absolute;
    top: 453px;
    left: 0;
    right: 0;
    display: flex;
    justify-content: space-between;
    align-items: baseline;
    padding: 0 8px;
    font-size: 7.5px;
  }
  .label__volume .fine { color: var(--muted); font-size: 4.5px; }
  .label__tab {
    position: absolute;
    left: 89px;
    top: 480px;
    width: 20px;
    height: 20px;
    background: var(--yellow);
  }
</style>
</head>
<body>
<main class="canvas">
  <h1 class="brand-mark">Copper<br>Wren</h1>

  <section class="label" aria-label="Mango pineapple bottle label">
    <p class="label__tagline">Copper Wren<br>from the<br>competition</p>
    <div class="label__fruit" role="img" aria-label="Photograph of whole mangoes, sliced pineapple rings and pineapples with green leaves stacked diagonally down the label"></div>
    <p class="label__name">Copper<br>Wren</p>
    <span class="flavor flavor--first">Mango</span>
    <span class="flavor flavor--second">Pineapple</span>
    <p class="label__type">Superfruit <em>Energy</em> Drink</p>
    <div class="label__volume">
      <span class="fine">made from concentrate</span>
      <span>500 mL (17.6 fl oz)</span>
      <span class="fine">fait de concentré</span>
    </div>
    <div class="label__tab"></div>
  </section>
</main>
</body>
</html>
```